Velvet Saturdays

Nightclub flyer. I'm one of the dj's but I want to do my own flyer for it as well. The night will feature dance/club music but I specialize in house/electronic music. Fall colors would be nice.

Target Market(s)

21-40 year olds who like club/dance/house music. We mainly want to appeal to the ladies

Industry/Entity Type

Club

Requirements
Must have
• VELVET Saturdays

Every Friday

Club Music:

DJQRZ
MOONGLIDER

House Music:

PARAGON
BELLO

123 Drink Specials & $4 Appetizer Specials till Midnight

$1-Draft Special
$2-Shot Special
$3-Well Special

$4-Appetizer Specials

21+
Doors Open @ 9pm
Plenty of FREE Parking

VIP/BIRTHDAYS/GROUPS/INFO
EMAIL: TRELLONIGHTEVENTS@ZUMVEX.COM

Inside Gumbleton's
512 Marlow Ave, Fairfield 94533
Nice to have
• I really like digital designs of girls like the vox lumea flyers, or outlines of the girls dancing or listening to music with headphones. This isn't mandatory but it's nice to see
Should not have
• While the flyer can feature a pretty, classy girl, I don't want anything too sexy/slutty for the girl. Also I don't like stars or wings.

```html
<!DOCTYPE html>
<html lang="en">
<head>
<meta charset="utf-8">
<title>Velvet Saturdays</title>
<link rel="stylesheet" href="https://fonts.googleapis.com/css2?family=Lilita+One&family=Anton&family=Roboto+Condensed:ital,wght@0,400;0,700;1,700&display=swap">
<style>
  :root {
    --paper: #f2f2f2;
    --ink: #1c1c1c;
    --title-yellow: #ffd21a;
    --title-orange: #f59a0c;
    --special-red: #d8121b;
    --name-yellow: #ffe10a;
    --white: #ffffff;
    --badge-red: #b3121a;
    --art-pink: #e2348f;
    --art-violet: #6a2c8e;
    --art-orange: #f28a1a;
    --art-teal: #1aa7c9;
    --art-green: #7cc242;
    --art-dark: #2a2a2a;
  }
  * { margin: 0; padding: 0; box-sizing: border-box; }
  html, body { width: 849px; height: 1200px; overflow: hidden; background: var(--paper); }
  .flyer {
    position: relative; width: 849px; height: 1200px; overflow: hidden;
    background: radial-gradient(circle at 50% 45%, #ffffff 0%, var(--paper) 55%, #d4d4d4 100%);
    font-family: "Roboto Condensed", sans-serif; color: var(--ink);
  }

  /* artwork placeholder: swirls, dancing girl, crowd, turntable */
  .artwork { position: absolute; inset: 0; }
  .artwork span { position: absolute; display: block; }
  .swirl-left {
    left: -40px; top: 330px; width: 420px; height: 360px; border-radius: 50%;
    background: conic-gradient(from 200deg, var(--art-teal), var(--art-green), var(--title-yellow), var(--art-orange), var(--art-pink), var(--art-teal));
    opacity: .75;
  }
  .swirl-right {
    right: -60px; top: 340px; width: 380px; height: 420px; border-radius: 50%;
    background: conic-gradient(from 20deg, var(--art-orange), var(--title-yellow), var(--art-green), var(--art-teal), var(--art-violet), var(--art-orange));
    opacity: .75;
  }
  .figure {
    left: 170px; top: 330px; width: 470px; height: 640px;
    border-radius: 48% 52% 40% 40% / 40% 40% 30% 30%;
    background: linear-gradient(170deg, #7a2a1a 0%, var(--art-pink) 38%, #c21f7a 70%, var(--art-violet) 100%);
  }
  .crowd {
    left: 0; top: 780px; width: 560px; height: 420px;
    border-radius: 60% 40% 0 0 / 30% 30% 0 0;
    background: linear-gradient(180deg, var(--art-orange), #e0601a);
  }
  .turntable {
    right: 0; top: 930px; width: 300px; height: 180px;
    border-radius: 50% 0 0 0 / 40% 0 0 0;
    background: linear-gradient(160deg, #5a5a5a, var(--art-dark));
  }

  .masthead { position: absolute; top: 10px; width: 100%; text-align: center; }
  .title {
    font-family: "Lilita One", sans-serif; line-height: .88; color: var(--title-yellow);
    -webkit-text-stroke: 3px var(--ink); paint-order: stroke fill;
    text-shadow: 0 5px 0 var(--title-orange);
  }
  .title-main { display: block; font-size: 96px; letter-spacing: 3px; }
  .title-sub { display: block; font-size: 68px; }
  .frequency { position: absolute; top: 172px; width: 100%; text-align: center;
    font-family: "Anton", sans-serif; font-size: 40px; letter-spacing: 1px; line-height: 1.1; }
  .specials-lead { position: absolute; top: 226px; width: 100%; text-align: center;
    color: var(--special-red); font-weight: 700; font-size: 26px; }
  .specials-list { position: absolute; top: 278px; width: 100%; text-align: center;
    font-weight: 700; font-size: 21px; }

  .lineup { position: absolute; left: 280px; top: 588px; width: 520px; text-align: center; }
  .genre { font-style: italic; font-weight: 700; font-size: 44px; color: var(--white);
    -webkit-text-stroke: 1px var(--ink); paint-order: stroke fill;
    text-shadow: 2px 2px 3px rgba(0,0,0,.6); line-height: 1.1; }
  .act { font-family: "Anton", sans-serif; font-size: 62px; color: var(--name-yellow);
    -webkit-text-stroke: 3px var(--ink); paint-order: stroke fill; line-height: 1.08; letter-spacing: 1px;
    text-shadow: 3px 3px 0 var(--ink); }
  .partner { position: absolute; left: 690px; top: 835px; width: 100px; height: 100px;
    border-radius: 50%; background: var(--ink); border: 3px solid var(--white);
    display: flex; align-items: center; justify-content: center;
    color: var(--white); font-weight: 700; font-size: 22px; }

  .entry-badge { position: absolute; left: 0; top: 985px; width: 210px; height: 215px;
    background: var(--badge-red); border-top-right-radius: 100px 70px;
    color: var(--white); text-align: center; padding-top: 18px; }
  .age { font-family: "Anton", sans-serif; font-size: 60px; line-height: 1; }
  .doors { font-weight: 700; font-size: 26px; line-height: 1.05; }
  .parking { font-style: italic; font-weight: 700; font-size: 18px; margin-top: 6px; line-height: 1.1; }

  .contact { position: absolute; left: 300px; top: 1108px; width: 549px; height: 82px;
    background: var(--white); padding: 0 14px; display: flex; align-items: center; gap: 12px;
    border-top-left-radius: 6px; border-bottom-left-radius: 6px; }
  .contact-lines { flex: 0 0 auto; border-right: 3px solid var(--ink); padding-right: 12px; }
  .contact-head { font-weight: 700; font-size: 25px; line-height: 1.1; }
  .contact-email { font-weight: 700; font-size: 13px; white-space: nowrap; }
  .venue { flex: 1 1 auto; font-size: 14px; font-weight: 700; line-height: 1.25; }
</style>
</head>
<body>
<main class="flyer">
  <div class="artwork" role="img" aria-label="Rainbow swirls around a girl dancing with headphones, an orange crowd silhouette bottom left and a DJ turntable bottom right">
    <span class="swirl-left" aria-hidden="true"></span>
    <span class="swirl-right" aria-hidden="true"></span>
    <span class="crowd" aria-hidden="true"></span>
    <span class="figure" aria-hidden="true"></span>
    <span class="turntable" aria-hidden="true"></span>
  </div>

  <header class="masthead">
    <h1 class="title"><span class="title-main">VELVET</span><span class="title-sub">Saturdays</span></h1>
  </header>
  <p class="frequency">EVERY FRIDAY</p>
  <p class="specials-lead">'123 Drink Specials &amp; $4 Appetizer Specials till Midnight</p>
  <p class="specials-list">$1-Draft Special • $2-Shot Special • $3-Well Special • $4-Appetizer Specials</p>

  <section class="lineup">
    <p class="genre">Club Music:</p>
    <p class="act">DJQRZ MOONGLIDER</p>
    <p class="genre">House Music:</p>
    <p class="act">PARAGON BELLO</p>
  </section>
  <div class="partner">BELLO</div>

  <aside class="entry-badge">
    <p class="age">21+</p>
    <p class="doors">Doors Open<br>@ 9pm</p>
    <p class="parking">Plenty of<br>FREE Parking</p>
  </aside>

  <footer class="contact">
    <div class="contact-lines">
      <p class="contact-head">VIP/BIRTHDAYS/GROUPS/INFO</p>
      <p class="contact-email">EMAIL: TRELLONIGHTEVENTS@ZUMVEX.COM</p>
    </div>
    <p class="venue">Inside Gumbleton's<br>512 Marlow Ave,<br>Fairfield 94533</p>
  </footer>
</main>
</body>
</html>
```